Discreet simple classy for adult entertainment

I would like a matte black business card with gold writing for my business. Keeping it simple. Having my following:

Lana frost
Events. Entertainment. Promotions
0491726580

or alternatively could have what i had on my previous card below but i think i prefer the above as again - discretion.

Maybe a nice gold line thru the card or some other very simple design . Or not open to ideas/ can be doublesided if any good ideas with that.

included pics of my old bus card. not sure weather i want a photo on it or not. if i do it wont be the same pic. i kinda wanted a card that was discreet so if it was in someones wallet they wouldn't neccessarily realise it was from a stripper.

Target Market(s)

men

Industry/Entity Type

Business

Contact Information for Business Card

Lana frost
0491726580

Requirements
Nice to have
• i don't know i am really open to anything. im giving my cards to guys so something they can have in their wallet that is discreet preferably.

```html
<!DOCTYPE html>
<html lang="en">
<head>
<meta charset="UTF-8">
<title>Lana Frost — Business Card</title>
<link rel="stylesheet" href="https://fonts.googleapis.com/css2?family=Michroma&family=Source+Sans+3:wght@400&display=swap">
<style>
  :root {
    --backdrop: #141414;
    --card-gold: #e8b414;
    --card-gold-light: #f2c63a;
    --card-gold-deep: #d9a60e;
    --ink: #111111;
    --emboss: #c9980c;
  }
  * { margin: 0; padding: 0; box-sizing: border-box; }
  html, body {
    width: 1200px;
    height: 900px;
    overflow: hidden;
    background: var(--backdrop);
  }
  .stage {
    position: relative;
    width: 1200px;
    height: 900px;
  }
  .card {
    position: absolute;
    top: 306px;
    width: 440px;
    height: 271px;
    overflow: hidden;
    background: var(--card-gold);
  }
  .card--front { left: 149px; }
  .card--back { left: 608px; }
  .card__texture {
    position: absolute;
    inset: 0;
    background:
      radial-gradient(ellipse at 20% 10%, var(--card-gold-light) 0%, transparent 45%),
      radial-gradient(ellipse at 85% 90%, var(--card-gold-light) 0%, transparent 40%),
      linear-gradient(160deg, var(--card-gold) 0%, var(--card-gold-deep) 100%);
    opacity: 0.9;
  }
  .card__content {
    position: absolute;
    inset: 0;
    text-align: center;
    color: var(--ink);
  }
  .card__name {
    position: absolute;
    left: 0; right: 0;
    top: 77px;
    font-family: "Michroma", sans-serif;
    font-size: 24px;
    letter-spacing: 1px;
    text-transform: uppercase;
  }
  .card__phone {
    position: absolute;
    left: 0; right: 0;
    top: 130px;
    font-family: "Source Sans 3", sans-serif;
    font-size: 25px;
  }
  .card__tagline {
    position: absolute;
    left: 0; right: 0;
    top: 179px;
    font-family: "Source Sans 3", sans-serif;
    font-size: 15px;
  }
  .card__wordmark {
    position: absolute;
    left: 0; right: 0;
    top: 113px;
    font-family: "Michroma", sans-serif;
    font-size: 35px;
    letter-spacing: 1px;
    text-transform: uppercase;
    color: var(--emboss);
  }
</style>
</head>
<body>
  <main class="stage">
    <section class="card card--front">
      <div class="card__texture" role="img" aria-label="Soft golden bokeh light texture"></div>
      <div class="card__content">
        <h1 class="card__name">Lana Frost</h1>
        <p class="card__phone">0491726580</p>
        <p class="card__tagline">Events. Entertainment. Promotions</p>
      </div>
    </section>
    <section class="card card--back">
      <div class="card__texture" role="img" aria-label="Soft golden bokeh light texture"></div>
      <div class="card__content">
        <p class="card__wordmark">Lana Frost</p>
      </div>
    </section>
  </main>
</body>
</html>
```